Stationary & Business Card for a Rock climbing company based primarily in Joshua Tree NP
Use provided logo
Stationary & Business Card for a Rock climbing company based primarily in Joshua Tree NP - Outdoors
Creative Brief
Simple
Garrick Fenn
Director
27615 Marrow Lane Victorville, CA 92307
garrickfenn@mailbrook.com
www.ridgepathoutfitters.com

```html
<!DOCTYPE html>
<html lang="en">
<head>
<meta charset="utf-8">
<title>Ridgepath Outfitters – Business Card</title>
<link href="https://fonts.googleapis.com/css2?family=Open+Sans:wght@400;600;700&display=swap" rel="stylesheet">
<style>
  :root {
    --stage: #8a8b8d;
    --card: #ffffff;
    --brown: #3b2216;
    --orange: #f2961e;
    --ink: #3a2a22;
    --muted: #5a4a42;
  }
  * { margin: 0; padding: 0; box-sizing: border-box; }
  html, body {
    width: 1200px; height: 908px; overflow: hidden;
    background: var(--stage);
    font-family: "Open Sans", Arial, sans-serif;
  }
  .canvas {
    width: 1200px; height: 908px;
    display: flex; flex-direction: column; align-items: center; justify-content: center;
    gap: 28px;
  }
  .card {
    position: relative;
    width: 700px; height: 400px;
    background: var(--card);
    border-radius: 22px;
    overflow: hidden;
    box-shadow: 0 6px 18px rgba(0,0,0,.25);
  }
  .brand {
    display: flex; align-items: center; gap: 14px;
    color: var(--ink); font-weight: 700; letter-spacing: .04em; text-transform: uppercase;
  }
  .brand__dot { border-radius: 50%; background: var(--orange); flex: none; }
  .card--front { display: flex; align-items: center; justify-content: center; }
  .card--front .brand { font-size: 34px; }
  .card--front .brand__dot { width: 60px; height: 60px; }

  .band { position: absolute; inset: 0; }
  .person { position: absolute; left: 30px; bottom: 42px; }
  .person__name { color: #fff; font-size: 24px; font-weight: 600; }
  .person__role { color: var(--orange); font-size: 18px; font-weight: 600; }

  .card--back .brand { position: absolute; right: 40px; top: 48px; font-size: 22px; }
  .card--back .brand__dot { width: 40px; height: 40px; }

  .contact {
    position: absolute; left: 290px; top: 168px;
    list-style: none; color: var(--muted); font-size: 17px; line-height: 1.5;
  }
  .contact li { display: flex; align-items: center; gap: 10px; }
  .contact .plain { padding-left: 0; }
  .icon { width: 18px; height: 18px; flex: none; }
</style>
</head>
<body>
<main class="canvas">
  <section class="card card--front">
    <div class="brand"><span class="brand__dot"></span>Ridgepath Outfitters</div>
  </section>

  <section class="card card--back">
    <svg class="band" width="700" height="400" viewBox="0 0 700 400">
      <path d="M0 0 H262 C205 130 232 270 182 400 H0 Z" fill="var(--orange)"/>
      <path d="M0 0 H252 C195 130 222 270 172 400 H0 Z" fill="#fff"/>
      <path d="M0 0 H240 C183 130 210 270 160 400 H0 Z" fill="var(--brown)"/>
    </svg>
    <div class="person">
      <p class="person__name">Garrick Fenn</p>
      <p class="person__role">Director</p>
    </div>
    <div class="brand"><span class="brand__dot"></span>Ridgepath Outfitters</div>
    <ul class="contact">
      <li class="plain">27615 Marrow Lane</li>
      <li class="plain">Victorville, CA 92307</li>
      <li>
        <svg class="icon" viewBox="0 0 18 18"><circle cx="9" cy="9" r="9" fill="var(--orange)"/><path d="M6 4.5 L7.6 4.5 L8.2 7 L7 7.8 Q8 10 10.2 11 L11 9.8 L13.5 10.4 L13.5 12 Q13 13.5 11 13.2 Q5.5 12 4.8 6.5 Q4.6 4.8 6 4.5Z" fill="#fff"/></svg>
        (760) 555-0148
      </li>
      <li>
        <svg class="icon" viewBox="0 0 18 18"><circle cx="9" cy="9" r="9" fill="var(--orange)"/><rect x="6" y="4" width="6" height="10" rx="1.2" fill="#fff"/><rect x="7" y="5.5" width="4" height="6" fill="var(--orange)"/></svg>
        (760) 555-0192
      </li>
      <li>
        <svg class="icon" viewBox="0 0 18 18"><circle cx="9" cy="9" r="9" fill="var(--orange)"/><rect x="4" y="5.5" width="10" height="7" rx="1" fill="#fff"/><path d="M4.5 6 L9 9.5 L13.5 6" stroke="var(--orange)" stroke-width="1" fill="none"/></svg>
        garrickfenn@mailbrook.com
      </li>
      <li>
        <svg class="icon" viewBox="0 0 18 18"><circle cx="9" cy="9" r="9" fill="var(--orange)"/><circle cx="9" cy="9" r="4.5" stroke="#fff" stroke-width="1.2" fill="none"/><path d="M4.5 9 H13.5 M9 4.5 V13.5" stroke="#fff" stroke-width="1"/></svg>
        www.ridgepathoutfitters.com
      </li>
    </ul>
  </section>
</main>
</body>
</html>
```